Web project update | ||
Q Dynamics eCommerce Template | ||
Computers | ||
www.qhalvorn.com | ||
We are manufacturer's representatives and power quality solution integrators. Our products and solutions address every aspect of power quality, distribution, and monitoring. | ||
Like: - Creative images/text - Simplicity - Sleek images/colors - Color Gradients - Corporate layout Dislike: - Clutter - Unnecessary Elements - Old-fashioned - Boring |
Cutting-Edge Clean/Simple Professional Corporate High Tech |
Blue | ||
Gray/Silver | ||
below header | ||
http://store.birchvale.com | ||
http://www.kestrova.com/ | ||
http://www.lumidex.com/ | ||
In order to match color scheme see our attached logo. We are going to need three things:A homepage for our store, a second-level page for our products to be displayed and a third page strictly used for information. Each main category will include a slideshow below the navigation, so make sure to leave plenty of room. Attempt to utilize a large amount of page width. The main inspiration for the template should come from Birchvale's online store. |
Téléchargez le matériel du projet |
850445_9152_6630.png Our Logo |
QDYN_LOGO_FOR_WEB_6830.zip here is our recently reproduced logo for the web. Please use this file. |
q_dyn_footerlogo_6881.png This is the image we would like to use as a footer logo. Scale to fit. |
Workers_6914.jpg Picture 1 |
Orvik_datacenter_2people_6915.jpg Picture 2 |
Orvik_Family_02_08_6916.jpg Picture 3 |
Orvik_Black_Product_Family__no_labels_6917.jpg Picture 4 |

```html
<!DOCTYPE html>
<html lang="en">
<head>
<meta charset="utf-8">
<title>Q Dynamics Store</title>
<link href="https://fonts.googleapis.com/css2?family=Arimo:wght@400;700&display=swap" rel="stylesheet">
<style>
:root{
  --page-bg:#d9dadc;
  --blue-dark:#0a3d8f;
  --blue:#1758c2;
  --blue-light:#3c86e6;
  --orange:#f07a10;
  --orange-light:#ffa53a;
  --text:#333;
  --muted:#777;
  --line:#d6d6d6;
  --white:#fff;
}
*{box-sizing:border-box;margin:0;padding:0}
html,body{width:1200px;height:959px;overflow:hidden}
body{background:linear-gradient(#eceded,var(--page-bg));font-family:"Arimo",Arial,sans-serif;color:var(--text);font-size:11px;position:relative}
.page{position:absolute;left:220px;top:0;width:760px;height:959px;background:var(--white);box-shadow:0 0 8px rgba(0,0,0,.2)}
.top-links{position:absolute;right:12px;top:6px;font-size:9px;color:var(--muted)}
.brand{position:absolute;left:22px;top:60px;display:flex;align-items:center;gap:7px;font-size:20px;font-weight:700;color:var(--blue)}
.brand-mark{width:16px;height:16px;background:var(--orange)}
.phone{position:absolute;left:486px;top:70px;font-size:12px;font-weight:700;color:var(--blue-dark)}
.cart{position:absolute;left:585px;top:67px;display:flex;align-items:center;gap:5px;font-size:11px;font-weight:700;color:var(--blue-dark)}
.nav{position:absolute;left:0;top:96px;width:100%;height:26px;background:linear-gradient(var(--blue-light),var(--blue-dark))}
.nav a{position:absolute;top:8px;color:var(--white);font-weight:700;font-size:9px;text-decoration:none}
.search{position:absolute;left:606px;top:5px;width:84px;height:16px;background:var(--white);border-radius:8px;font-size:8px;color:#999;padding:3px 8px}
.sidebar{position:absolute;left:13px;top:150px;width:177px}
.side-head{height:26px;border-radius:4px;background:linear-gradient(var(--orange-light),var(--orange));color:var(--white);font-weight:700;font-size:11px;display:flex;align-items:center;padding-left:10px;gap:7px}
.side-head .dot{width:8px;height:8px;border-radius:50%;background:var(--white)}
.cat-list{list-style:none;border:1px solid var(--line);border-top:0}
.cat-list li{height:22px;line-height:22px;border-bottom:1px solid #eee;padding-left:18px;font-size:8.5px;color:#444;position:relative;white-space:nowrap}
.cat-list li::before{content:"";position:absolute;left:8px;top:8px;border-left:5px solid var(--orange);border-top:3px solid transparent;border-bottom:3px solid transparent}
.care{margin-top:10px;height:98px;border:1px solid var(--line);border-radius:4px;position:relative;background:linear-gradient(#fff,#f1f1f1)}
.care-photo{position:absolute;left:5px;bottom:0;width:52px;height:86px;background:linear-gradient(#e9d8c6,#c8a88a);border-radius:4px 4px 0 0}
.care-text{position:absolute;right:10px;top:10px;text-align:right}
.care-text small{display:block;font-size:9px;color:var(--muted)}
.care-text b{display:block;font-size:13px;color:var(--orange);line-height:1.15}
.care-text .num{font-size:16px;color:var(--blue);font-weight:700;margin-top:4px}
.newsletter{margin-top:10px}
.newsletter-body{border:1px solid var(--line);border-top:0;height:58px;padding:10px;font-size:8.5px;color:var(--muted);position:relative}
.field{border-bottom:1px solid var(--line);padding-bottom:4px;width:110px}
.btn{display:inline-block;background:linear-gradient(var(--orange-light),var(--orange));color:var(--white);font-size:8px;font-weight:700;border-radius:3px;padding:3px 9px}
.newsletter-body .btn{position:absolute;right:8px;bottom:8px}
.cards{margin-top:10px}
.cards-body{border:1px solid var(--line);border-top:0;height:34px;display:flex;gap:5px;align-items:center;justify-content:center}
.cards-body span{width:22px;height:14px;border-radius:2px;background:#c9d3e2}
.main{position:absolute;left:203px;top:150px;width:546px}
.banner{height:182px;border-radius:6px;background:linear-gradient(135deg,#f69a2a,#e05e05);position:relative;overflow:hidden}
.banner h2{position:absolute;left:30px;top:20px;color:var(--white);font-size:20px;line-height:1.15;font-weight:700}
.banner p{position:absolute;left:30px;top:78px;width:250px;color:#ffe9d2;font-size:8px;line-height:1.45}
.banner-product{position:absolute;right:36px;top:18px;width:150px;height:146px;background:linear-gradient(#4a4d52,#1e1f22);border-radius:4px}
.dots{position:absolute;left:130px;bottom:10px;display:flex;gap:5px}
.dots i{width:6px;height:6px;border-radius:50%;background:#ffd1a3}
.dots i:first-child{background:var(--white)}
.ribbon{position:absolute;right:0;top:0;width:34px;height:34px;background:var(--orange-light);clip-path:polygon(0 0,100% 0,100% 100%)}
.welcome{margin-top:14px}
.welcome h1{font-size:15px;font-weight:400;color:#222}
.welcome h1 span{color:var(--orange)}
.welcome hr{border:0;border-top:1px solid var(--line);margin:7px 0 8px}
.welcome p{font-size:8.5px;line-height:1.45;color:#555;margin-bottom:7px}
.featured{margin-top:12px;border:1px solid var(--line);border-radius:5px;height:272px}
.featured h3{font-size:11px;font-weight:400;padding:9px 12px;border-bottom:1px solid var(--line);background:linear-gradient(#fff,#f0f0f0)}
.products{display:flex;justify-content:space-around;padding:16px 8px}
.product{width:150px;text-align:center}
.product h4{font-size:8px;font-weight:400;color:#444;margin-bottom:8px}
.product-img{height:118px;border:1px solid #eee;border-radius:4px;background:linear-gradient(#fff,#f2f2f2);position:relative}
.product-img::after{content:"";position:absolute;left:40px;top:36px;width:70px;height:46px;background:linear-gradient(#55585e,#222);border-radius:3px}
.actions{margin-top:10px;display:flex;flex-direction:column;align-items:center;gap:5px}
.btn-gray{display:inline-block;background:linear-gradient(#8a8d92,#5a5d62);color:var(--white);font-size:8px;border-radius:3px;padding:3px 12px}
.footer{position:absolute;left:0;bottom:0;width:100%;height:125px;background:linear-gradient(var(--blue),var(--blue-dark));color:var(--white);font-size:8px}
.footer h5{color:var(--orange-light);font-size:10px;margin-bottom:8px}
.foot-nav{position:absolute;left:18px;top:12px;display:grid;grid-template-columns:80px 80px;row-gap:6px}
.foot-news{position:absolute;left:273px;top:12px;width:330px}
.foot-news div{margin-bottom:8px;line-height:1.4}
.foot-brand{position:absolute;right:14px;top:18px;text-align:right}
.foot-brand strong{display:block;font-size:13px;margin-bottom:8px}
</style>
</head>
<body>
<div class="page">
  <div class="top-links">Home | FAQ | Contact Us</div>
  <header>
    <div class="brand"><span class="brand-mark"></span>Q Dynamics</div>
    <div class="phone">800.555.0199</div>
    <div class="cart">
      <svg width="16" height="14" viewBox="0 0 18 16"><path d="M1 2h3l2 8h9l2-6H5" fill="none" stroke="#0a3d8f" stroke-width="1.6"/><circle cx="7" cy="13.5" r="1.5" fill="#0a3d8f"/><circle cx="14" cy="13.5" r="1.5" fill="#0a3d8f"/></svg>
      Product Cart: (0) Items
    </div>
  </header>
  <nav class="nav">
    <a style="left:26px">HOME</a><a style="left:90px">SOLUTIONS</a><a style="left:195px">PRODUCTS</a><a style="left:290px">SERVICES</a><a style="left:377px">KNOWLEDGE BASE</a><a style="left:515px">SUPPORT</a>
    <div class="search">Search</div>
  </nav>

  <aside class="sidebar">
    <div class="side-head"><span class="dot"></span>Browse by Category</div>
    <ul class="cat-list">
      <li>UPS SYSTEMS</li><li>RACK POWER PRODUCTS</li><li>ENCLOSURES</li><li>SURGE SUPPRESSION</li>
      <li>TRACK SWITCHES</li><li>COOLING PRODUCTS</li><li>RAISED FLOOR AIR GRATES</li><li>PDU CABLES</li>
      <li>BATTERIES</li><li>SOFTWARE SOLUTIONS</li><li>MONITORING SOLUTIONS</li><li>GENERATORS</li>
      <li>EPO PANELS &amp; BUTTONS</li><li>UPS BYPASS PANELS</li><li>SERVICES</li>
    </ul>
    <div class="care">
      <div class="care-photo" role="img" aria-label="Customer care agent with headset"></div>
      <div class="care-text"><small>Have Question?</small><b>Customer Care<br>Center</b><div class="num">800.555.0199</div></div>
    </div>
    <div class="newsletter">
      <div class="side-head"><span class="dot"></span>Subscribe Newsletter</div>
      <div class="newsletter-body"><div class="field">Enter email address...</div><span class="btn">Subscribe</span></div>
    </div>
    <div class="cards">
      <div class="side-head"><span class="dot"></span>Credit Card Services</div>
      <div class="cards-body"><span></span><span></span><span></span><span></span></div>
    </div>
  </aside>

  <main class="main">
    <section class="banner">
      <h2>Extends UPS service life<br>with user-replaceable batteries</h2>
      <p>Lorem ipsum dolor sit amet, consectetur adipisicing elit, sed do eiusmod tempor incididunt ut labore et dolore magna aliqua. Ut enim ad minim veniam, quis nostrud exercitation ullamco laboris nisi ut aliquip ex ea commodo consequat.</p>
      <div class="banner-product" role="img" aria-label="Family of black UPS units and a rack cabinet"></div>
      <div class="ribbon"></div>
      <div class="dots"><i></i><i></i><i></i><i></i></div>
    </section>
    <section class="welcome">
      <h1>Welcome to <span>Q Dynamics</span></h1>
      <hr>
      <p>Lorem ipsum dolor sit amet, consectetur adipisicing elit, sed do eiusmod tempor incididunt ut labore et dolore magna aliqua Ut enim ad minim veniam, quis nostrud exercitation ullam.</p>
      <p>Ut enim ad minim veniam, quis nostrud exercitation ullamco laboris nisi ut aliquip ex ea commodo consequat. Duis aute irure dolor in reprehenderit in voluptate velit esse cillum dolore eu fugiat nulla pariatur. Excepteur sint occaecat cupidatat non proident, sunt in culpa qui officia deserunt mollit anim id est laborum. Lorem ipsum dolor sit amet, consectetur adipisicing elit, sed do eiusmod tempor incididunt ut labore et dolore magna aliqua.</p>
    </section>
    <section class="featured">
      <h3>Featured Products</h3>
      <div class="products">
        <div class="product"><h4>Q100 UPS (500-700 VA)</h4><div class="product-img" role="img" aria-label="Compact UPS unit"></div><div class="actions"><span class="btn">Add to Cart</span><span class="btn-gray">Details</span></div></div>
        <div class="product"><h4>QX UPS (5 - 20 kVA)</h4><div class="product-img" role="img" aria-label="Rack UPS unit"></div><div class="actions"><span class="btn">Add to Cart</span><span class="btn-gray">Details</span></div></div>
        <div class="product"><h4>QX UPS (5 - 20 kVA)</h4><div class="product-img" role="img" aria-label="Rack UPS unit"></div><div class="actions"><span class="btn">Add to Cart</span><span class="btn-gray">Details</span></div></div>
      </div>
    </section>
  </main>

  <footer class="footer">
    <div class="foot-nav">
      <h5 style="grid-column:1/3">Navigation</h5>
      <span>› Home</span><span>› Knowledge Base</span>
      <span>› Solutions</span><span>› Support</span>
      <span>› Products</span><span>› Contact Us</span>
      <span>› Services</span>
    </div>
    <div class="foot-news">
      <h5>News</h5>
      <div><b>19-5-2011</b><br>Lorem ipsum dolor sit amet, consectetur adipisicing elit sed do.</div>
      <div><b>19-5-2011</b><br>Lorem ipsum dolor sit amet, consectetur adipisicing elit sed do.</div>
    </div>
    <div class="foot-brand"><strong>Q Dynamics</strong>Copyright © 2011,<br>Q Dynamics, Inc.<br>All rights reserved.</div>
  </footer>
</div>
</body>
</html>
```